GUARANTEED! Simple website for independent event planner and consultant...

I need a website that is no more than 5 or 6 pages to illustrate who I am and what I can offer to groups who book hotels for meetings and conferences. I have 20 years of experience planning meetings within hotels and I am now ready to go out on my own and help clients choose venues, negotiate contracts and plan effective meetings. I will focus on clients planning meetings in the mountains of Colorado but I am willing to travel as well. I want to work with a person who is collaborative and can direct me on what they need to move the project along quickly. I already have my logo, a hosting site and work e-mail address. Also, I recently hired a photographer to do head shots. Lastly, it important for me to be able to talk on the phone or skype with this person, as needed and I must be able to make changes to my site down the road when necessary...

Target Market(s)

Corporate Groups

Industry/Entity Type

Event Planning

Coding

Coded - Design and coding required

Number of Pages Required

5+ page

Font styles to use
Sans Serif

Requirements
Must have
• About me page, event planning services offered page, task force and consulting work page, testimonials page, page for blogs, page to contact me/request a proposal. May need advice on what else I need...
Nice to have
• I want it to look sharp and professional. I want people to look at my site and know immediately that they can trust me and the work I can do.
• I don't want it to look like it is over the top as I am not a HUGE company but I do want it to be professional and easy to view and navigate.
Should not have
• Bright colors
• My logo is bright orange and black. I have also used dark grey and orange. See below:
• Orange:
• C = 0
• M = 64
• Y = 100
• K = 0
• Gray:
• C = 67
• M = 60
• Y = 59
• K = 45
• Font: Gotham Book and Gotham Bold

```html
<!DOCTYPE html>
<html lang="en">
<head>
<meta charset="utf-8">
<title>Alder Event Management</title>
<link href="https://fonts.googleapis.com/css2?family=Montserrat:wght@300;400;500;600;700&family=Dancing+Script:wght@700&display=swap" rel="stylesheet">
<style>
:root{
  --orange:#f47b20;
  --ink:#333333;
  --text:#555555;
  --card:#3d3d3d;
  --band:#f2f2f2;
  --footer:#2b2b2b;
  --footer-line:#444444;
  --bottom:#1f1f1f;
  --white:#ffffff;
}
*{box-sizing:border-box;margin:0;padding:0}
html,body{width:1200px;height:2320px;overflow:hidden;background:var(--white)}
body{position:relative;font-family:'Montserrat',Arial,sans-serif;color:var(--text)}
.abs{position:absolute}
a{color:inherit;text-decoration:none}
h1,h2,h3,h4{font-weight:400}

/* hero */
.hero{left:0;top:0;width:1200px;height:515px;overflow:hidden}
.hero-photo{left:0;top:0;width:1200px;height:515px;
  background:linear-gradient(180deg,#f4f6f8 0%,#dde3ea 18%,#8a98aa 40%,#2f3f57 70%,#1d2a3e 100%)}
.hero-shade{left:0;top:120px;width:1200px;height:395px;background:linear-gradient(180deg,rgba(20,30,50,0) 0%,rgba(20,30,50,.35) 100%)}
.brand{left:217px;top:34px;color:var(--orange);font-weight:700;font-size:18px;line-height:22px;letter-spacing:1px;text-transform:uppercase;white-space:nowrap;display:flex;align-items:flex-start;gap:8px}
.brand-mark{display:block;width:14px;height:14px;background:var(--orange);margin-top:4px;flex:none}
.social-top{left:764px;top:24px;display:flex;gap:8px}
.social-top span{width:24px;height:24px;background:var(--orange);display:block}
.call{left:862px;top:24px;width:122px;height:24px;border:1px solid var(--orange);background:var(--white);font-size:10px;color:var(--ink);line-height:22px;padding-left:8px;white-space:nowrap}
.call b{font-weight:700}
.call svg{position:absolute;right:8px;top:8px}
.mail-top{left:725px;top:53px;width:260px;text-align:right;font-size:10px;color:var(--ink);white-space:nowrap}
.nav{left:440px;top:106px;display:flex;gap:17px;font-size:9.5px;text-transform:uppercase;color:var(--ink);font-weight:500;white-space:nowrap}
.nav .on{border-bottom:2px solid var(--orange);padding-bottom:6px}
.nav-line{left:440px;top:128px;width:545px;height:1px;background:#c9cfd6}
.hero-title{left:0;top:330px;width:1200px;text-align:center;color:var(--white);font-weight:300;font-size:30px;letter-spacing:1px;text-transform:uppercase}
.hero-sub{left:0;top:372px;width:1200px;text-align:center;color:var(--white);font-weight:700;font-size:14.5px;line-height:23px;text-transform:uppercase;letter-spacing:.2px}
.btn-dark{left:560px;top:427px;width:81px;height:27px;border:2px solid var(--orange);background:rgba(0,0,0,.55);color:var(--white);font-size:9px;font-weight:700;text-transform:uppercase;text-align:center;line-height:23px}

/* welcome */
.welcome-title{left:217px;top:555px;font-size:20px;color:var(--ink)}
.welcome-title b{color:var(--orange);font-weight:600}
.welcome-body{left:217px;top:590px;width:540px;font-size:10px;line-height:17px;color:var(--text)}
.welcome-body p{margin-bottom:17px}
.portrait{left:217px;top:803px;width:145px;height:184px;background:linear-gradient(160deg,#d9d9d9,#8a8a8a 60%,#3a3a3a)}
.planner-name{left:374px;top:838px;font-size:17px;font-weight:600;color:var(--orange)}
.planner-cred{left:374px;top:864px;font-size:8px;font-weight:700;color:var(--ink)}
.planner-role{left:374px;top:876px;font-size:8px;color:var(--orange);text-transform:uppercase}
.planner-bio{left:374px;top:904px;width:382px;font-size:10px;line-height:17px;color:var(--ink)}
.planner-bio .more{color:var(--orange);font-weight:700;text-transform:uppercase;font-size:9px}

.proposal{left:775px;top:560px;width:209px;height:427px;background:var(--orange);padding:14px 11px}
.proposal h2{color:var(--white);font-size:15px;font-weight:700;text-transform:uppercase;line-height:20px;white-space:nowrap}
.proposal .lead{color:var(--ink);font-size:9.5px;margin-top:2px}
.proposal .rule{height:1px;background:rgba(255,255,255,.45);margin:10px 0 12px}
.field{height:38px;background:var(--white);border:3px solid #f9b27a;margin-bottom:14px;font-size:9.5px;color:#777;padding:10px 6px}
.field.msg{height:124px}
.submit{width:118px;height:44px;background:var(--card);color:var(--white);font-size:19px;font-weight:700;text-align:center;line-height:40px;border:2px solid #f9b27a;text-transform:uppercase}

/* services */
.section-title{left:0;width:1200px;text-align:center;font-size:20px;color:var(--ink)}
.section-title b{color:var(--orange);font-weight:600}
.services-title{top:1061px}
.services-intro{left:217px;top:1092px;width:767px;text-align:center;font-size:10px;line-height:17px}
.services-band{left:0;top:1140px;width:1200px;height:412px;background:var(--band)}
.card{top:1171px;width:163px;height:289px;background:var(--card);border-top:4px solid var(--orange)}
.card h3{position:absolute;left:10px;top:12px;width:140px;color:var(--orange);font-size:14.5px;font-weight:600;line-height:17px;height:52px;display:flex;align-items:flex-end}
.card p{position:absolute;left:10px;top:82px;width:145px;color:#ddd;font-size:9.5px;line-height:14px}
.card .learn{position:absolute;left:10px;top:142px;color:var(--white);font-size:9.5px;text-decoration:underline}
.card .shot{position:absolute;left:0;bottom:0;width:163px;height:115px}
.arrow{top:1298px}
.btn-outline{left:501px;top:1489px;width:199px;height:31px;border:2px solid var(--orange);background:var(--white);color:var(--ink);font-size:9.5px;font-weight:700;text-transform:uppercase;text-align:center;line-height:27px;white-space:nowrap}

/* orange band */
.orange-band{left:0;top:1552px;width:1200px;height:329px;background:var(--orange)}
.band-title{font-size:20px;color:var(--white)}
.band-title b{font-weight:600}
.band-lead{font-size:9.5px;color:var(--ink)}
.client-photo{left:244px;top:1646px;width:106px;height:125px;background:linear-gradient(170deg,#e8e8e8,#9aa4b0 55%,#2c3e5c);border:3px solid var(--white)}
.testimonial-text{left:362px;top:1645px;width:380px}
.quote{font-family:'Dancing Script',cursive;font-size:16px;line-height:20px;color:var(--ink)}
.quote-body{margin-top:6px;font-size:10px;line-height:16px;color:var(--white)}
.quote-name{margin-top:5px;font-size:9px;font-weight:700;color:var(--ink);text-transform:uppercase;line-height:12px}
.quote-name span{display:block;font-weight:400;text-transform:none;color:#5a3210}
.band-link{font-size:9.5px;color:var(--ink)}
.post{left:775px;width:210px;height:86px}
.post .thumb{position:absolute;left:0;top:0;width:59px;height:78px;background:linear-gradient(180deg,#dfe7f0,#7f92ad 60%,#40536f)}
.post h4{position:absolute;left:66px;top:0;width:145px;color:var(--white);font-size:9.5px;font-weight:700;line-height:12px}
.post .date{position:absolute;left:66px;top:26px;font-size:8px;color:var(--ink)}
.post p{position:absolute;left:66px;top:38px;width:145px;font-size:8.5px;line-height:11px;color:var(--white)}

/* footer */
.footer{left:0;top:1881px;width:1200px;height:396px;background:var(--footer)}
.foot-head{top:1962px;color:var(--white);font-size:13px;border-left:3px solid var(--orange);padding-left:6px;line-height:15px}
.map{left:217px;top:1990px;width:198px;height:94px;background:linear-gradient(135deg,#f0eeea,#d9d6cf)}
.contact-list{left:217px;top:2096px;width:220px;font-size:9.5px;color:#ccc;line-height:14px}
.contact-list .phone{color:var(--orange);font-size:16px;margin:10px 0 12px;display:flex;align-items:center;gap:6px}
.contact-list .row{display:flex;gap:6px;align-items:flex-start}
.dot{width:7px;height:7px;border-radius:50%;background:var(--orange);margin-top:3px;flex:none}
.links{width:146px;font-size:9.5px;color:#ccc}
.links li{list-style:none;border-bottom:1px solid var(--footer-line);padding:7px 8px 9px;line-height:13px}
.btn-foot{left:450px;top:2164px;width:165px;height:31px;border:2px solid var(--orange);color:var(--white);font-size:9.5px;font-weight:700;text-transform:uppercase;text-align:center;line-height:27px;white-space:nowrap}
.social-foot{left:815px;top:2017px;display:flex;gap:9px}
.social-foot span{width:25px;height:25px;border-radius:50%;background:var(--orange);display:block}
.foot-brand{left:820px;top:2102px;color:#4e4e4e;font-size:16px;font-weight:700;text-transform:uppercase;line-height:20px;letter-spacing:1px;white-space:nowrap}
.bottom{left:0;top:2277px;width:1200px;height:43px;background:var(--bottom);font-size:9.5px;color:#888;text-align:center;line-height:43px}
.bottom b{color:var(--orange);font-weight:400}
</style>
</head>
<body>

<header class="abs hero">
  <div class="abs hero-photo" role="img" aria-label="Photo of an empty boardroom with a long conference table and leather chairs"></div>
  <div class="abs hero-shade"></div>
  <div class="abs brand"><span class="brand-mark"></span><span>Alder<br>Event Management</span></div>
  <div class="abs social-top" aria-label="Social links"><span></span><span></span><span></span></div>
  <div class="abs call">Call: <b>555.014.2290</b>
    <svg width="8" height="6" viewBox="0 0 8 6"><path d="M1 1l3 3 3-3" fill="none" stroke="#333" stroke-width="1.3"/></svg>
  </div>
  <div class="abs mail-top">✉ dana@aldereventmanagement.com</div>
  <nav class="abs nav">
    <a class="on">Home</a><a>About Me</a><a>Services</a><a>Task Force &amp; Consulting</a><a>Testimonials</a><a>Blog</a><a>Contact Me</a>
  </nav>
  <div class="abs nav-line"></div>
  <h1 class="abs hero-title">Alder Event Management</h1>
  <p class="abs hero-sub">Specializes in event management for associations, corporations, not for profit<br>companies and personal social events of all sizes in the state of Colorado.</p>
  <a class="abs btn-dark">Know More</a>
</header>

<section>
  <h2 class="abs welcome-title">Welcome to <b>Alder Event Management</b></h2>
  <div class="abs welcome-body">
    <p>Do you ever wish that you could shift the event planning responsibilities for your company to another person who excels in the management of all details associated with putting on a great meeting or event?</p>
    <p>Well, you can...<br>Alder Event Management specializes in event management for associations, corporations, not for profit companies and personal social events of all sizes in the state of Colorado.</p>
    <p>If planning events for your company takes you away from larger initiatives you manage day to day let us take on the burden. We guarantee that our experience inside the property walls will benefit you and your company on many levels.</p>
  </div>
  <div class="abs portrait" role="img" aria-label="Black and white headshot of the event planner"></div>
  <h3 class="abs planner-name">Dana Whitfield</h3>
  <div class="abs planner-cred">CMP, CMM</div>
  <div class="abs planner-role">Event Planner and Consultant</div>
  <p class="abs planner-bio">After a successful 20+ year career coordinating events in the resort community of Vail, Dana is now providing her skills on the other side of the table.<br>When you hire Alder Event Management you are hiring a company who is intimately familiar with the inner-workings of hotels, resorts and off-site hospitality venues. You will be working with an event... <a class="more">Read More ›</a></p>

  <form class="abs proposal">
    <h2>Request a Proposal</h2>
    <div class="lead">Lorem ipsum dolor sit amet</div>
    <div class="rule"></div>
    <div class="field">Name:</div>
    <div class="field">Email:</div>
    <div class="field">Phone:</div>
    <div class="field msg">Message:</div>
    <div class="submit">Submit</div>
  </form>
</section>

<section>
  <h2 class="abs section-title services-title">Services <b>Offered</b></h2>
  <p class="abs services-intro">Lorem Ipsum is simply dummy text of the printing and typesetting industry. Lorem Ipsum has been the industry's standard dummy text ever since the 1500s, when an unknown printer took a galley of type and scrambled it to make a type specimen book.</p>
  <div class="abs services-band"></div>
  <svg class="abs arrow" style="left:218px" width="20" height="36" viewBox="0 0 20 36"><path d="M18 1L2 18l16 17" fill="none" stroke="#bbb" stroke-width="1.5"/></svg>
  <svg class="abs arrow" style="left:962px" width="20" height="36" viewBox="0 0 20 36"><path d="M2 1l16 17L2 35" fill="none" stroke="#bbb" stroke-width="1.5"/></svg>

  <article class="abs card" style="left:257px">
    <h3>Site Inspections and Venue Selection</h3>
    <p>Lorem Ipsum is simply dummy text of the printing and typesetting industry.</p>
    <a class="learn">Learn More</a>
    <div class="shot" role="img" aria-label="Photo of a resort pool with palm trees at dusk" style="background:linear-gradient(180deg,#4a5a78,#2a2f3d 55%,#a5683a)"></div>
  </article>
  <article class="abs card" style="left:431px">
    <h3>Contract Negotiations</h3>
    <p>Lorem Ipsum is simply dummy text of the printing and typesetting industry.</p>
    <a class="learn">Learn More</a>
    <div class="shot" role="img" aria-label="Photo of a hand signing a contract" style="background:linear-gradient(160deg,#f2f2f2,#cfcfcf 60%,#b08f7a)"></div>
  </article>
  <article class="abs card" style="left:606px">
    <h3>Food and<br>Beverage</h3>
    <p>Lorem Ipsum is simply dummy text of the printing and typesetting industry.</p>
    <a class="learn">Learn More</a>
    <div class="shot" role="img" aria-label="Photo of plated dishes on a wooden table" style="background:linear-gradient(135deg,#6b4a32,#c69a5a 50%,#7a5840)"></div>
  </article>
  <article class="abs card" style="left:781px">
    <h3>Agenda Creation and Progam Planning</h3>
    <p>Lorem Ipsum is simply dummy text of the printing and typesetting industry.</p>
    <a class="learn">Learn More</a>
    <div class="shot" role="img" aria-label="Photo of a team planning around a desk" style="background:linear-gradient(135deg,#8a7a68,#d9d2c8 55%,#5a5048)"></div>
  </article>
  <a class="abs btn-outline">Know More About Our Services</a>
</section>

<section>
  <div class="abs orange-band"></div>
  <h2 class="abs band-title" style="left:217px;top:1570px">What Our Clients <b>Say About Us</b></h2>
  <p class="abs band-lead" style="left:217px;top:1598px">Lorem Ipsum is simply dummy text of the printing and typesetting industry.</p>
  <svg class="abs" style="left:216px;top:1701px" width="10" height="14" viewBox="0 0 10 14"><path d="M10 0v14L0 7z" fill="#333"/></svg>
  <svg class="abs" style="left:742px;top:1701px" width="10" height="14" viewBox="0 0 10 14"><path d="M0 0v14l10-7z" fill="#333"/></svg>
  <div class="abs client-photo" role="img" aria-label="Portrait photo of a client in a suit"></div>
  <div class="abs testimonial-text">
    <p class="quote">"Lorem Ipsum is simply dummy text of the printing and typesetting industry.</p>
    <p class="quote-body">Lorem Ipsum is simply dummy text of the printing and typesetting industry. Lorem Ipsum has been the industry's standard dummy text ever since the 1500s, when an unknown printer took a galley of type and scrambled.</p>
    <div class="quote-name">Paul Hendry<span>CEO, Northline Company</span></div>
  </div>
  <a class="abs band-link" style="left:217px;top:1841px">More Testimonials ›</a>

  <h2 class="abs band-title" style="left:775px;top:1570px">Latest <b>Blog Posts</b></h2>
  <p class="abs band-lead" style="left:775px;top:1598px">Lorem Ipsum is simply dummy text</p>
  <article class="abs post" style="top:1624px">
    <div class="thumb" role="img" aria-label="Photo of a business presentation"></div>
    <h4>Contrary to popular belief, Lorem Ipsum.</h4>
    <div class="date">July 10, 2017 &nbsp;|&nbsp; Monday</div>
    <p>It has roots in a piece of classical Latin literature from 45 BC, making it over 2000 <u>Learn More</u></p>
  </article>
  <article class="abs post" style="top:1733px">
    <div class="thumb" role="img" aria-label="Photo of a business presentation"></div>
    <h4>Contrary to popular belief, Lorem Ipsum.</h4>
    <div class="date">July 10, 2017 &nbsp;|&nbsp; Monday</div>
    <p>It has roots in a piece of classical Latin literature from 45 BC, making it over 2000 <u>Learn More</u></p>
  </article>
  <a class="abs band-link" style="left:775px;top:1841px">More Blog Posts ›</a>
</section>

<footer>
  <div class="abs footer"></div>
  <h3 class="abs foot-head" style="left:217px">Contact Details</h3>
  <div class="abs map" role="img" aria-label="Street map showing the office location"></div>
  <div class="abs contact-list">
    <div class="row"><span class="dot"></span><span>PO Box 1200 Ridgeview, CO 80000<br>United States</span></div>
    <div class="phone"><svg width="11" height="11" viewBox="0 0 24 24"><path d="M6.6 10.8a15 15 0 006.6 6.6l2.2-2.2c.3-.3.7-.4 1-.2 1.1.4 2.3.6 3.6.6.6 0 1 .4 1 1V20c0 .6-.4 1-1 1A17 17 0 013 4c0-.6.4-1 1-1h3.5c.6 0 1 .4 1 1 0 1.3.2 2.5.6 3.6.1.3 0 .7-.2 1z" fill="#f47b20"/></svg>555.010.4400</div>
    <div class="row"><span class="dot"></span><span>mail@aldereventmanagement.com</span></div>
    <div class="row"><span class="dot"></span><span>www.aldereventmanagement.com</span></div>
  </div>

  <h3 class="abs foot-head" style="left:450px">Quick Links</h3>
  <ul class="abs links" style="left:450px;top:1990px">
    <li>About</li><li>Services</li><li>Task Force &amp; Consulting</li><li>Testimonials</li><li>Blog</li><li>Contact Me</li>
  </ul>
  <a class="abs btn-foot">Request for Proposal</a>

  <h3 class="abs foot-head" style="left:647px">Specialties</h3>
  <ul class="abs links" style="left:647px;top:1990px">
    <li>Site Inspections and Venue Selection</li><li>Contract Negotiations</li><li>Food and Beverage</li><li>Agenda Creation and Progam Planning</li><li>AudioVisual Expertise</li><li style="border:0;color:#f47b20">More...</li>
  </ul>

  <h3 class="abs foot-head" style="left:815px">Social Media</h3>
  <p class="abs" style="left:822px;top:1993px;font-size:9.5px;color:#ccc">Lorem ipsum dolor sit amet.</p>
  <div class="abs social-foot" aria-label="Social links"><span></span><span></span><span></span><span></span><span></span></div>
  <div class="abs foot-brand">Alder<br>Event Management</div>

  <div class="abs bottom">Copyright © 2017, <b>Alder Event Management</b>. All Rights Reserved.</div>
</footer>

</body>
</html>
```